Hollow Fern Kentucky Bourbon Whiskey

We need a label design for a bottle of whiskey. It is for a 750 ml bottle and needs to have a place to write in proof, age, and bottle number at bottom of label. It is a single barrel bourbon. We want to include our tree logo attached in the upload files in some way. Leave out the Distillery part to where it just says Hollow Fern Bourbon Whiskey with the tree. We need the label to be clean and modern. I have also attached a picture of the bottle the label is intended to go on.

Industry/Entity Type

Bourbon

Requirements
Must have
• Hollow Fern tree from file

```html
<!DOCTYPE html>
<html lang="en">
<head>
<meta charset="utf-8">
<title>Hollow Fern Bourbon Whiskey – Label</title>
<link rel="stylesheet" href="https://fonts.googleapis.com/css2?family=Cinzel:wght@400;700;900&family=Yellowtail&family=Oswald:wght@300;400&display=swap">
<style>
  :root {
    --bg: #e6e6e6;
    --gold-light: #fbf3c4;
    --gold: #e6c978;
    --gold-deep: #b8862c;
    --cream: #f3e6b5;
    --red-hot: #e0100c;
    --red: #a80a08;
    --red-deep: #560303;
    --ink-brown: #3a2608;
  }
  * { box-sizing: border-box; margin: 0; padding: 0; }
  html, body { width: 753px; height: 1200px; overflow: hidden; background: var(--bg); }
  .canvas { position: relative; width: 753px; height: 1200px; }

  .gold-text {
    background: linear-gradient(180deg, var(--gold-light) 0%, var(--gold) 55%, var(--gold-deep) 100%);
    -webkit-background-clip: text; background-clip: text; color: transparent;
  }

  /* Neck label */
  .neck-label {
    position: absolute; left: 216px; top: 70px; width: 320px; height: 170px;
    background: linear-gradient(90deg, #e9d89a 0%, var(--gold-light) 45%, #efe0a8 100%);
    display: flex; flex-direction: column; align-items: center; justify-content: center;
  }
  .neck-rule { position: absolute; left: 0; right: 0; height: 3px; background: var(--gold-deep); }
  .neck-rule.r1 { top: 14px; } .neck-rule.r2 { top: 24px; }
  .neck-rule.r3 { bottom: 24px; } .neck-rule.r4 { bottom: 14px; }
  .neck-name { font-family: 'Cinzel', serif; font-weight: 700; font-size: 38px; color: var(--ink-brown); letter-spacing: 1px; line-height: 1; }
  .neck-sub { font-family: 'Cinzel', serif; font-weight: 400; font-size: 24px; color: var(--ink-brown); letter-spacing: 2px; margin-top: 8px; }

  /* Main round label */
  .main-label {
    position: absolute; left: 106px; top: 290px; width: 540px; height: 540px; border-radius: 50%;
    background: linear-gradient(135deg, var(--gold-light), var(--gold) 50%, var(--gold-deep));
    padding: 10px;
  }
  .main-face {
    width: 100%; height: 100%; border-radius: 50%;
    background: radial-gradient(circle at 55% 50%, var(--red-hot) 0%, var(--red) 45%, var(--red-deep) 100%);
    display: flex; flex-direction: column; align-items: center; text-align: center;
    padding-top: 118px;
  }
  .brand { display: flex; align-items: center; gap: 10px; }
  .brand-dot { width: 12px; height: 12px; border-radius: 50%; background: var(--cream); }
  .brand-name { font-family: 'Cinzel', serif; font-weight: 700; font-size: 30px; color: var(--cream); letter-spacing: 1px; }
  .product-script {
    font-family: 'Yellowtail', cursive; font-size: 128px; line-height: 1; margin-top: 6px;
    color: var(--gold-light); text-shadow: 3px 3px 0 var(--red-deep);
  }
  .product-type { font-family: 'Cinzel', serif; font-weight: 900; font-size: 46px; letter-spacing: 5px; color: var(--cream); margin-top: -4px; }
  .specs { font-family: 'Oswald', sans-serif; font-weight: 300; font-size: 22px; color: var(--cream); margin-top: 26px; line-height: 1.35; }
  .specs span + span { margin-left: 30px; }

  /* Bottom panel */
  .info-panel {
    position: absolute; left: 58px; top: 880px; width: 636px; height: 170px; border-radius: 34px;
    background: linear-gradient(135deg, var(--gold-light), var(--gold) 50%, var(--gold-deep));
    padding: 9px;
  }
  .info-face {
    width: 100%; height: 100%; border-radius: 26px;
    background: radial-gradient(ellipse at 50% 40%, var(--red-hot) 0%, var(--red) 45%, var(--red-deep) 100%);
    padding: 16px 30px 0;
  }
  .info-grid { display: grid; grid-template-columns: 1fr 1fr 1fr; margin: 0 40px; }
  .info-cell { text-align: center; font-family: 'Oswald', sans-serif; font-weight: 300; color: var(--cream); font-size: 22px; line-height: 1.25; padding-bottom: 6px; }
  .info-cell + .info-cell { border-left: 1px solid var(--cream); }
  .info-cell .key { display: inline-block; border-bottom: 1px solid var(--cream); padding: 0 8px; }
  .info-note {
    border-top: 1px solid var(--cream); padding-top: 6px;
    font-family: 'Cinzel', serif; font-size: 10.5px; line-height: 1.5; color: var(--cream); text-align: center; letter-spacing: 0.3px;
  }
</style>
</head>
<body>
<main class="canvas">
  <section class="neck-label">
    <span class="neck-rule r1"></span><span class="neck-rule r2"></span>
    <p class="neck-name">HOLLOW FERN</p>
    <p class="neck-sub">DISTILLERY</p>
    <span class="neck-rule r3"></span><span class="neck-rule r4"></span>
  </section>

  <section class="main-label">
    <div class="main-face">
      <div class="brand"><span class="brand-dot"></span><span class="brand-name">Hollow Fern</span></div>
      <h1 class="product-script">Whiskey</h1>
      <p class="product-type">BURBON</p>
      <p class="specs"><span>750ml</span><span>40% Alc /Vol</span><br>80 Proof</p>
    </div>
  </section>

  <section class="info-panel">
    <div class="info-face">
      <div class="info-grid">
        <div class="info-cell"><span class="key">REGION</span><br>USA</div>
        <div class="info-cell"><span class="key">HARVEST</span><br>2005</div>
        <div class="info-cell"><span class="key">BOTTLE</span><br>No-1</div>
      </div>
      <p class="info-note">This special whiskey is made using 80% rye, 18% corn and 12% barley. It has a stunningly fruity profile, offset by the heavy aromas of vanilla and honey obtained from the barrel, and the herbaceous spice that the rye grain</p>
    </div>
  </section>
</main>
</body>
</html>
```